Brightpath Letterhead

We would like a letterhead for our company. I have uploaded our logo.

Brightpath Ridge Consulting
1450 W Corliss Ave Ste 310
Arlington, TX 76006
833-517-2906

```html
<!DOCTYPE html>
<html lang="en">
<head>
<meta charset="utf-8">
<title>Brightpath Letterhead</title>
<link rel="stylesheet" href="https://fonts.googleapis.com/css2?family=Arimo:wght@400&family=PT+Sans:wght@400;700&display=swap">
<style>
  :root {
    --backdrop: #dcdddf;
    --paper: #f2f3f4;
    --ink: #4a4c4f;
    --ink-dark: #1d1f22;
    --teal: #154f5d;
    --green: #5db688;
    --white: #ffffff;
    --sign-tone: #dfe2e5;
  }
  * { margin: 0; padding: 0; box-sizing: border-box; }
  html, body {
    width: 1200px; height: 1141px; overflow: hidden;
    background: var(--backdrop);
  }
  .letterhead {
    position: absolute; left: 215px; top: 30px;
    width: 770px; height: 1081px;
    background: var(--paper);
    font-family: "Arimo", Arial, sans-serif;
    color: var(--ink);
    box-shadow: 0 2px 8px rgba(0,0,0,0.12);
    overflow: hidden;
  }
  .brand {
    position: absolute; left: 0; right: 0; top: 72px;
    display: flex; justify-content: center; align-items: center; gap: 12px;
  }
  .brand-mark {
    width: 44px; height: 44px; border-radius: 50%;
    background: var(--teal);
  }
  .brand-name {
    font-family: "PT Sans", Arial, sans-serif; font-weight: 700;
    color: var(--teal); text-transform: uppercase; line-height: 1.05;
  }
  .brand-name .line-main { display: block; font-size: 25px; letter-spacing: 2.5px; }
  .brand-name .line-sub { display: block; font-size: 18px; letter-spacing: 2.8px; }
  .greeting {
    position: absolute; left: 58px; top: 350px;
    font-size: 18px; color: var(--ink);
  }
  .letter-body {
    position: absolute; left: 58px; top: 403px; width: 656px;
    font-size: 11.2px; line-height: 16.4px; text-align: justify;
  }
  .letter-body p { margin-bottom: 16.4px; }
  .closing {
    position: absolute; left: 58px; top: 767px; font-size: 11.2px;
  }
  .signature {
    position: absolute; left: 58px; top: 796px; width: 82px; height: 32px;
    background: var(--sign-tone);
  }
  .contact {
    position: absolute; left: 0; right: 0; top: 1000px; text-align: center;
    font-family: "PT Sans", Arial, sans-serif;
  }
  .contact .address { font-size: 12px; color: var(--ink-dark); }
  .contact .phone { font-size: 15.5px; font-weight: 700; color: var(--teal); margin-top: 2px; letter-spacing: 0.3px; }
  .footer-band { position: absolute; left: 0; bottom: 0; width: 770px; height: 18px; }
</style>
</head>
<body>
  <main class="letterhead">
    <header class="brand">
      <div class="brand-mark"></div>
      <div class="brand-name">
        <span class="line-main">Brightpath Ridge</span>
        <span class="line-sub">Consulting</span>
      </div>
    </header>

    <p class="greeting">Dear Mr. Alden,</p>

    <section class="letter-body">
      <p>Lorem ipsum dolor sit amet, consectetur adipiscing elit. Donec orci purus, luctus vitae dignissim eu, iaculis sed purus. Vivamus faucibus, ipsum nec aliquet viverra, leo mauris condimentum ligula, sit amet sagittis enim ligula quis arcu. Nam egestas tortor id nisi porttitor mattis. In tortor ante, ultricies in suscipit a, tempus non massa. Vivamus et auctor mi. Fusce vel massa nulla. Phasellus nec eros mauris, et scelerisque orci.</p>
      <p>Donec malesuada orci vitae nulla accumsan porta a id massa. Quisque accumsan iaculis magna sit amet fringilla. Maecenas consequat, magna eget tincidunt semper, odio nibh rutrum mi, id feugiat ante nisi eu risus. Vestibulum nunc orci, rhoncus a placerat in, ultricies in mi. Cras mattis varius eros, vel fringilla nisi suscipit eget. Quisque scelerisque sagittis nulla at porttitor.</p>
      <p>Sed id augue vitae urna euismod commodo aliquet a quam. Pellentesque arcu velit, cursus et malesuada ut, consequat et diam. Nullam erat sem, rhoncus id ullamcorper vitae, rhoncus et arcu. In ultricies ultricies nulla, ut rutrum nisi iaculis at. Donec eu magna a metus ornare faucibus. Fusce aliquet faucibus ultricies. Morbi semper, est id tincidunt gravida, sem arcu adipiscing lacus, ac bibendum nulla leo eu purus. Quisque nec diam sed risus consectetur a ccumsan quis quis nibh. Vestibulum id purus lorem.</p>
      <p>It is a long established fact that a reader will be distracted by the readable content of a page when looking at its layout. The point of using Lorem Ipsum is that it has a more-or-less normal distribution of letters, as opposed to using ‘Content here, content here’, making it look like readable English. Many desktop publishing packages</p>
      <p>ada ut, consequat et diam. Nullam erat sem, rhoncus id ullamcorper vitae, rhoncus et arcu. In ultricies ultricies nulla, ut rutrum nisi iaculis at. Donec eu magna a metus ornare faucibus. Fusce aliquet faucibus ultricies. Morbi semper,</p>
    </section>

    <p class="closing">Sincerely,</p>
    <div class="signature" role="img" aria-label="Handwritten signature of the sender"></div>

    <footer class="contact">
      <p class="address">1450 W Corliss Ave Ste 310 , Arlington, TX 76006</p>
      <p class="phone">833-517-2906</p>
    </footer>

    <svg class="footer-band" viewBox="0 0 770 18" aria-hidden="true">
      <rect x="0" y="3" width="600" height="15" fill="var(--teal)"/>
      <rect x="600" y="3" width="170" height="15" fill="var(--green)"/>
      <polygon points="582,3 618,3 600,17" fill="var(--green)"/>
      <polyline points="582,3 600,17 618,3" fill="none" stroke="var(--white)" stroke-width="2"/>
    </svg>
  </main>
</body>
</html>
```